U.S. based testing, inspection, and certification (TIC) company needs a new social media design.

We need a social media design primarily for LinkedIn 1200x1200px for our U.S. based company with international capabilities for performing dozens if not hundreds of testing, inspection, and certification (TIC) services. Our primary services include calibration, chemical analysis, consulting engineering, environmental simulation, forensic engineering, materials testing, mechanical testing, and nondestructive testing. Industries we serve are aerospace/aviation, automotive, chemical, commercial properties, construction, consumer products, defense, energy storage, healthcare, insurance/legal, life science, manufacturing, oil & gas, power generation, pulp & paper, and telecommunications. https://veltrolabs.example/

Guideline hex colors (primary, secondary): #29aae2, #0b1f3b

The final design should communicate:
1. Trust, Integrity, and Independence
2. Technical Expertise and Accuracy
3. Efficiency and Speed
4. Value-Added Partnership

We previously used a hexagon design that we would like to part ways from; hexagon examples and KRV logos uploaded.

```html
<!DOCTYPE html>
<html lang="en">
<head>
<meta charset="utf-8">
<title>KRV – Independent Testing. Proven Accuracy.</title>
<link href="https://fonts.googleapis.com/css2?family=Montserrat:wght@400;500;600;700;800&display=swap" rel="stylesheet">
<style>
  :root{
    --navy:#0b1f3b;
    --navy-deep:#0c1a36;
    --sky:#29aae2;
    --hero-mid:#1d5a8c;
    --panel:#d5e1ed;
    --ink:#13284a;
    --icon:#1f8fd6;
    --white:#ffffff;
  }
  *{margin:0;padding:0;box-sizing:border-box}
  html,body{width:1200px;height:1200px;overflow:hidden;background:var(--navy)}
  .canvas{position:relative;width:1200px;height:1200px;font-family:"Montserrat",sans-serif;color:var(--white);overflow:hidden}

  .header{position:absolute;left:0;top:0;width:1200px;height:130px;background:var(--navy)}
  .brand{position:absolute;left:90px;top:34px;width:210px;display:flex;flex-direction:column;align-items:flex-start}
  .brand-name{font-size:62px;font-weight:800;letter-spacing:6px;line-height:62px;color:var(--white)}
  .brand-sub{font-size:15px;font-weight:500;line-height:20px;margin-top:2px;color:var(--white)}
  .tagline{position:absolute;left:373px;top:48px;font-size:40px;font-weight:400;letter-spacing:.5px;color:var(--white)}
  .header-rule{position:absolute;left:0;top:128px;width:1200px;height:2px;background:#1a3d66}
  .header-accent{position:absolute;left:0;top:130px;width:90px;height:14px;background:var(--sky)}

  .hero{position:absolute;left:0;top:130px;width:1200px;height:248px;
    background:linear-gradient(90deg,#0f2a50 0%,#17497a 45%,#2a6fa8 75%,#3785bd 100%)}
  .hero-lines{position:absolute;inset:0}
  .headline{position:absolute;left:92px;top:52px;font-size:58px;font-weight:800;line-height:56px;color:var(--white)}
  .services-line{position:absolute;left:96px;top:178px;font-size:23px;font-weight:700;color:var(--white)}
  .services-line .lead{color:var(--sky)}

  .photo-strip{position:absolute;left:0;top:378px;width:1200px;height:370px;display:block}

  .industries{position:absolute;left:0;top:748px;width:1200px;height:285px;background:var(--panel)}
  .industries-title{position:absolute;left:0;top:28px;width:1200px;text-align:center;font-size:24px;font-weight:700;color:var(--ink)}
  .service{position:absolute;display:flex;align-items:center;gap:16px;font-size:23px;font-weight:500;line-height:28px;color:var(--ink)}
  .service svg{flex:none;width:40px;height:40px}
  .divider{position:absolute;width:1px;height:64px;background:#9fb2c6}

  .footer{position:absolute;left:0;top:1033px;width:1200px;height:167px;background:var(--navy-deep)}
  .footer-rule{position:absolute;left:0;top:0;width:1200px;height:8px;background:linear-gradient(90deg,#1d6fae,var(--sky) 50%,#1d6fae)}
  .footer-lines{position:absolute;inset:0}
  .cta{position:absolute;left:0;top:48px;width:1200px;text-align:center;font-size:28px;font-weight:400}
  .cta strong{font-weight:700}
  .url{position:absolute;left:0;top:99px;width:1200px;text-align:center;font-size:28px;font-weight:600;color:var(--sky)}
</style>
</head>
<body>
<div class="canvas">

  <header class="header">
    <div class="brand">
      <span class="brand-name">KRV</span>
      <span class="brand-sub">Veltro Technical Services</span>
    </div>
    <div class="tagline">Testing · Inspection · Certification</div>
    <div class="header-rule"></div>
  </header>

  <section class="hero">
    <svg class="hero-lines" width="1200" height="248" viewBox="0 0 1200 248" aria-hidden="true">
      <g fill="none" stroke="#4f9fd6" stroke-opacity=".35" stroke-width="2">
        <path d="M820 88 H1120 L1150 58 H1200"/>
        <path d="M860 110 H1200"/>
        <path d="M940 140 H1080 L1110 170 H1200"/>
        <path d="M900 200 H1050 L1080 230 H1200"/>
        <path d="M60 224 H880 L910 190"/>
      </g>
      <g stroke="#7fc0ea" stroke-opacity=".35" stroke-width="3">
        <path d="M710 44 l10 -14 M722 44 l10 -14 M734 44 l10 -14 M746 44 l10 -14 M758 44 l10 -14 M770 44 l10 -14 M782 44 l10 -14 M794 44 l10 -14 M806 44 l10 -14 M818 44 l10 -14 M830 44 l10 -14 M842 44 l10 -14 M854 44 l10 -14 M866 44 l10 -14 M878 44 l10 -14"/>
      </g>
    </svg>
    <div class="header-accent" style="top:0"></div>
    <h1 class="headline">Independent Testing.<br>Proven Accuracy.</h1>
    <p class="services-line"><span class="lead">Calibration</span> ·&nbsp; Materials Testing · Forensic Engineering · NDT</p>
  </section>

  <svg class="photo-strip" viewBox="0 0 1200 370" role="img" aria-label="Four angled photo panels: a passenger jet landing against a blue sky, a technician analysing data on lab monitors, automated test machinery in a laboratory, and an engineer in hard hat and safety vest holding a tablet on a factory floor">
    <defs>
      <linearGradient id="sky" x1="0" y1="0" x2="0" y2="1"><stop offset="0" stop-color="#4e88c4"/><stop offset="1" stop-color="#9cc3e6"/></linearGradient>
      <linearGradient id="lab" x1="0" y1="0" x2="1" y2="1"><stop offset="0" stop-color="#6d9cc6"/><stop offset="1" stop-color="#c9d8e6"/></linearGradient>
      <linearGradient id="mach" x1="0" y1="0" x2="1" y2="1"><stop offset="0" stop-color="#3c5f86"/><stop offset="1" stop-color="#8fa9c3"/></linearGradient>
      <linearGradient id="plant" x1="0" y1="0" x2="1" y2="1"><stop offset="0" stop-color="#5f7f9e"/><stop offset="1" stop-color="#b9a36a"/></linearGradient>
    </defs>
    <rect width="1200" height="370" fill="#1a4a7a"/>
    <polygon points="0,0 380,0 220,370 0,370" fill="url(#sky)"/>
    <polygon points="385,0 728,0 555,370 225,370" fill="url(#lab)"/>
    <polygon points="733,0 925,0 745,370 560,370" fill="url(#mach)"/>
    <polygon points="930,0 1200,0 1200,370 750,370" fill="url(#plant)"/>
  </svg>

  <section class="industries">
    <h2 class="industries-title">Serving Critical Industries</h2>

    <div class="service" style="left:120px;top:90px">
      <svg viewBox="0 0 40 40" fill="none" stroke="var(--icon)" stroke-width="2.4"><path d="M2 10V2h8M30 2h8v8M38 30v8h-8M10 38H2v-8"/><circle cx="20" cy="20" r="10"/><circle cx="20" cy="20" r="4" fill="var(--icon)"/><path d="M20 6v6M20 28v6M6 20h6M28 20h6"/></svg>
      <span>Calibration</span>
    </div>
    <div class="divider" style="left:325px;top:82px"></div>

    <div class="service" style="left:358px;top:88px">
      <svg viewBox="0 0 40 40" fill="none" stroke="var(--icon)" stroke-width="2.4"><path d="M10 3h10M12 3v12L3 35h24L18 15V3"/><path d="M7 27h16" /><path d="M28 12h9v22a4 4 0 0 1-9 0z"/><circle cx="33" cy="5" r="2"/></svg>
      <span>Chemical<br>Analysis</span>
    </div>
    <div class="divider" style="left:587px;top:82px"></div>

    <div class="service" style="left:604px;top:88px">
      <svg viewBox="0 0 40 40"><ellipse cx="20" cy="10" rx="18" ry="6" fill="var(--icon)"/><rect x="2" y="10" width="36" height="14" fill="var(--icon)"/><ellipse cx="20" cy="24" rx="18" ry="6" fill="var(--icon)"/><path d="M12 16l6-5 5 4 5-3" stroke="#fff" stroke-width="2" fill="none"/><rect x="10" y="31" width="8" height="6" rx="2" fill="none" stroke="var(--icon)" stroke-width="2"/><rect x="22" y="31" width="8" height="6" rx="2" fill="none" stroke="var(--icon)" stroke-width="2"/></svg>
      <span>Environmental<br>Simulation</span>
    </div>
    <div class="divider" style="left:867px;top:82px"></div>

    <div class="service" style="left:888px;top:84px">
      <svg viewBox="0 0 40 40" fill="none" stroke="var(--icon)" stroke-width="2.4"><rect x="3" y="3" width="24" height="32" rx="2"/><path d="M8 10h4M15 10h8M8 17h4M15 17h8M8 24h4"/><circle cx="29" cy="28" r="6"/><path d="M33 32l5 5"/></svg>
      <span>Material<br>Testing</span>
    </div>

    <div class="service" style="left:123px;top:169px">
      <svg viewBox="0 0 40 40" fill="none" stroke="var(--icon)" stroke-width="2.4"><path d="M4 12l14-6 4 8-14 6z"/><circle cx="30" cy="10" r="4"/><path d="M22 12l6-1M16 20l4 10M12 37h16M20 30v7"/><circle cx="20" cy="30" r="2"/></svg>
      <span>Mechanical<br>Testing</span>
    </div>
    <div class="divider" style="left:325px;top:163px"></div>

    <div class="service" style="left:358px;top:169px">
      <svg viewBox="0 0 40 40" fill="none" stroke="var(--icon)" stroke-width="2.4"><path d="M26 4l10 10M28 8l-14 14-4 0 0-4L24 4"/><path d="M10 22l-4 4"/><circle cx="6" cy="32" r="2.5"/><circle cx="14" cy="34" r="1.5"/><circle cx="8" cy="12" r="1.5"/></svg>
      <span>Forensic<br>Engineering</span>
    </div>
    <div class="divider" style="left:587px;top:163px"></div>

    <div class="service" style="left:608px;top:169px">
      <svg viewBox="0 0 40 40" fill="none" stroke="var(--icon)" stroke-width="2.4"><path d="M3 36h34"/><rect x="7" y="16" width="6" height="20"/><rect x="17" y="8" width="6" height="28"/><rect x="27" y="20" width="6" height="16"/><path d="M20 2v6M5 24h30"/></svg>
      <span>Non destructive<br>Testing</span>
    </div>
    <div class="divider" style="left:867px;top:163px"></div>

    <div class="service" style="left:884px;top:165px">
      <svg viewBox="0 0 40 40"><circle cx="14" cy="24" r="11" fill="var(--icon)"/><circle cx="14" cy="24" r="4" fill="var(--panel)"/><circle cx="30" cy="12" r="8" fill="var(--icon)"/><circle cx="30" cy="12" r="3" fill="var(--panel)"/><circle cx="31" cy="31" r="5" fill="var(--icon)"/><circle cx="31" cy="31" r="2" fill="var(--panel)"/></svg>
      <span>Consulting<br>Engineering</span>
    </div>
  </section>

  <footer class="footer">
    <svg class="footer-lines" width="1200" height="167" viewBox="0 0 1200 167" aria-hidden="true">
      <g fill="none" stroke="#2a4a72" stroke-opacity=".6" stroke-width="2">
        <path d="M0 30 H400 M20 70 H150 L180 100 H260 V167 M960 40 H1200 M1000 140 H1120 L1150 110 H1200"/>
      </g>
    </svg>
    <div class="footer-rule"></div>
    <p class="cta">Partner with a <strong>Trusted Independent Laboratory</strong></p>
    <p class="url">veltrolabs.example</p>
  </footer>

</div>
</body>
</html>
```